iOS page Redesign

Need a page to be redesigned for the app. The app helps users find caregivers for Senior and Child. Note that text "Enter Booking Date" has to be removed and that line with date and time stays. If possible I would like a 24 hr turnaround on this task.

Target Market(s)

Families looking for child and senior care

Industry/Entity Type

Childcare

Requirements
Must have
• Colour as per the app screen shot and color scheme

```html
<!DOCTYPE html>
<html lang="en">
<head>
<meta charset="utf-8">
<title>Search Caregivers</title>
<link href="https://fonts.googleapis.com/css2?family=Raleway:wght@400;500;600&display=swap" rel="stylesheet">
<style>
  :root {
    --purple: #6b5b8e;
    --purple-text: #6b5b8e;
    --field: #e1e1e1;
    --mint: #c8e4da;
    --ink: #3a3a3a;
    --placeholder: #b3b3b3;
    --star: #dedede;
    --divider: #dcdcdc;
    --white: #ffffff;
  }
  * { box-sizing: border-box; margin: 0; padding: 0; }
  html, body { width: 675px; height: 1200px; overflow: hidden; background: var(--white); }
  body { font-family: "Raleway", "Helvetica Neue", sans-serif; font-variant-numeric: lining-nums; color: var(--ink); }
  .screen { position: relative; width: 675px; height: 1200px; overflow: hidden; background: var(--white); }

  .top-bar { position: absolute; left: 0; top: 0; width: 675px; height: 119px; background: var(--purple); color: var(--white); }
  .status-bar { position: absolute; left: 0; top: 0; width: 675px; height: 32px; font-size: 17px; font-weight: 600; }
  .status-carrier { position: absolute; left: 14px; top: 5px; display: flex; align-items: center; gap: 6px; }
  .status-time { position: absolute; left: 0; width: 675px; top: 5px; text-align: center; }
  .status-right { position: absolute; right: 14px; top: 6px; }
  .nav-title { position: absolute; left: 0; width: 675px; top: 66px; text-align: center; font-size: 29px; font-weight: 400; letter-spacing: 0.3px; }
  .nav-menu { position: absolute; left: 27px; top: 70px; }
  .nav-refresh { position: absolute; left: 557px; top: 68px; }
  .nav-bell { position: absolute; left: 619px; top: 66px; }

  .field { position: absolute; left: 0; width: 675px; background: var(--field); color: var(--placeholder); font-size: 26px; padding-left: 31px; display: flex; align-items: center; }
  .field-name { top: 120px; height: 67px; }
  .field-address { top: 192px; height: 69px; }

  .date-box { position: absolute; top: 288px; height: 69px; background: var(--field); font-size: 29px; display: flex; align-items: center; justify-content: center; word-spacing: 6px; }
  .date-start { left: 0; width: 334px; }
  .date-end { left: 341px; width: 334px; }

  .care-label { position: absolute; left: 0; width: 675px; top: 378px; text-align: center; font-size: 27px; color: var(--purple-text); }
  .care-option { position: absolute; top: 430px; height: 105px; font-size: 29px; display: flex; align-items: center; justify-content: center; }
  .care-senior { left: 0; width: 337px; background: var(--field); color: var(--ink); }
  .care-child { left: 337px; width: 338px; background: var(--purple); color: var(--white); }

  .search-button { position: absolute; left: 0; top: 544px; width: 675px; height: 69px; background: var(--mint); color: var(--purple-text); font-size: 29px; display: flex; align-items: center; justify-content: center; gap: 18px; }

  .caregiver { position: absolute; left: 0; width: 675px; height: 135px; }
  .caregiver::after { content: ""; position: absolute; left: 29px; right: 29px; bottom: 0; height: 1px; background: var(--divider); }
  .caregiver-avatar { position: absolute; left: 22px; top: 12px; width: 115px; height: 115px; border-radius: 50%; }
  .caregiver-name { position: absolute; left: 160px; top: 26px; font-size: 28px; font-weight: 500; }
  .caregiver-rating { position: absolute; left: 160px; top: 70px; display: flex; gap: 11px; }
  .caregiver-price { position: absolute; right: 37px; top: 45px; font-size: 28px; font-weight: 500; }
</style>
</head>
<body>
<main class="screen">
  <header class="top-bar">
    <div class="status-bar">
      <div class="status-carrier">
        <svg width="44" height="10" viewBox="0 0 44 10"><g fill="#fff"><circle cx="4" cy="5" r="4"/><circle cx="13" cy="5" r="4"/></g><g fill="none" stroke="#fff" stroke-width="1"><circle cx="22" cy="5" r="3.5"/><circle cx="31" cy="5" r="3.5"/><circle cx="40" cy="5" r="3.5"/></g></svg>
        <span>Telvia</span>
        <svg width="18" height="14" viewBox="0 0 18 14"><path d="M9 13 L1 4 A12 12 0 0 1 17 4 Z" fill="#fff"/></svg>
      </div>
      <div class="status-time">14:39</div>
      <div class="status-right">
        <svg width="72" height="20" viewBox="0 0 72 20"><circle cx="8" cy="10" r="7" fill="none" stroke="#fff" stroke-width="2"/><rect x="5" y="9" width="6" height="5" fill="#fff"/><rect x="26" y="3" width="40" height="15" rx="3" fill="none" stroke="#fff" stroke-width="1.5"/><rect x="28" y="5" width="15" height="11" fill="#fff"/><rect x="67" y="8" width="3" height="5" fill="#fff"/></svg>
      </div>
    </div>
    <svg class="nav-menu" width="42" height="30" viewBox="0 0 42 30"><g fill="#fff"><rect y="0" width="42" height="4"/><rect y="13" width="42" height="4"/><rect y="26" width="42" height="4"/></g></svg>
    <div class="nav-title">Search Caregivers</div>
    <svg class="nav-refresh" width="34" height="34" viewBox="0 0 34 34"><g fill="none" stroke="#fff" stroke-width="4.5"><path d="M6 20 A11 11 0 0 1 25 8"/><path d="M28 14 A11 11 0 0 1 9 26"/></g><path d="M21 2 L31 8 L21 14 Z" fill="#fff"/><path d="M13 20 L3 26 L13 32 Z" fill="#fff"/></svg>
    <svg class="nav-bell" width="32" height="36" viewBox="0 0 32 36"><path d="M16 3 C9 3 6 9 6 15 L6 23 L2 28 L30 28 L26 23 L26 15 C26 9 23 3 16 3 Z" fill="#fff"/><circle cx="16" cy="31" r="4" fill="#fff"/></svg>
  </header>

  <div class="field field-name">Search by Caregiver Name (Optional)</div>
  <div class="field field-address">Job address (if different then home address)</div>

  <div class="date-box date-start">09/12&nbsp; 08:00 AM</div>
  <div class="date-box date-end">10/12&nbsp; 16:00 PM</div>

  <div class="care-label">Choose Type Of Care</div>
  <div class="care-option care-senior">Senior Care</div>
  <div class="care-option care-child">Child Care</div>

  <div class="search-button">
    <svg width="34" height="34" viewBox="0 0 34 34"><circle cx="14" cy="14" r="10.5" fill="none" stroke="#6b5b8e" stroke-width="4"/><path d="M22 22 L31 31" stroke="#6b5b8e" stroke-width="5" stroke-linecap="round"/></svg>
    <span>Search</span>
  </div>

  <section class="caregiver" style="top:629px">
    <div class="caregiver-avatar" role="img" aria-label="Profile photo of a baby wrapped in a pink blanket" style="background: radial-gradient(circle at 55% 50%, #f3dde4 0%, #d9c6bd 55%, #5b4a40 100%);"></div>
    <div class="caregiver-name">Lindel care</div>
    <svg class="caregiver-rating" width="226" height="28" viewBox="0 0 226 28"><defs><path id="star" d="M14 1 L17.6 10 L27 10.4 L19.7 16.4 L22.2 26 L14 20.6 L5.8 26 L8.3 16.4 L1 10.4 L10.4 10 Z" fill="#dedede"/></defs><use href="#star"/><use href="#star" x="37"/><use href="#star" x="74"/><use href="#star" x="111"/><use href="#star" x="148"/></svg>
    <div class="caregiver-price">$30/hr</div>
  </section>

  <section class="caregiver" style="top:764px">
    <div class="caregiver-avatar" role="img" aria-label="Orsa Child care logo area" style="background: #f2f2f2;"></div>
    <div class="caregiver-name">Orsa Child care</div>
    <svg class="caregiver-rating" width="226" height="28" viewBox="0 0 226 28"><use href="#star"/><use href="#star" x="37"/><use href="#star" x="74"/><use href="#star" x="111"/><use href="#star" x="148"/></svg>
    <div class="caregiver-price">$20/hr</div>
  </section>

  <section class="caregiver" style="top:899px">
    <div class="caregiver-avatar" role="img" aria-label="Pell Babyyy Care logo area" style="background: radial-gradient(circle, #fbe7b0 0%, #e8f0f8 100%);"></div>
    <div class="caregiver-name">Pell Babyyy Care</div>
    <svg class="caregiver-rating" width="226" height="28" viewBox="0 0 226 28"><use href="#star"/><use href="#star" x="37"/><use href="#star" x="74"/><use href="#star" x="111"/><use href="#star" x="148"/></svg>
    <div class="caregiver-price">$20/hr</div>
  </section>

  <section class="caregiver" style="top:1034px">
    <div class="caregiver-avatar" role="img" aria-label="B7 Prism Care logo area" style="background: linear-gradient(160deg, #f7a531 0%, #fbe3b4 60%, #f05a2a 100%);"></div>
    <div class="caregiver-name">B7 Prism Care</div>
    <svg class="caregiver-rating" width="226" height="28" viewBox="0 0 226 28"><use href="#star"/><use href="#star" x="37"/><use href="#star" x="74"/><use href="#star" x="111"/><use href="#star" x="148"/></svg>
    <div class="caregiver-price">$40/hr</div>
  </section>

  <section class="caregiver" style="top:1172px">
    <div class="caregiver-avatar" role="img" aria-label="Caregiver profile image" style="background: #ececec; top:13px;"></div>
  </section>
</main>
</body>
</html>
```